out of the box Business Card Design for a Manufacturer / Distributor

We are a manufarturer and distributor of products.
the company name is VORTANI (Pic attached)

the picture is NOT a must have on the business Card.

the Business Card should look really professional and/or special, so out of the box thinking is welcome.

there should be 2 Adresses on the Business Card for Main and Branch Office.
Email Adress, homepage, Name is required
NO Phone Number

Our working field:
Private Labeling
high Quality Production
direct distribution
warehousing
trademark registration
legal support

Main Office:
Kornblumenweg 14
08352 Lindenfeld
Germany

Branch Office:
Daska Lane
Rahimabad
Pakistan

Names:
Lukas Feldhaus (Owner)
Imran Qureshi (Owner)

Email:
lukas@vortani-example.com
imran@vortani-example.com

homepage:
vortani-example.com

Industry/Entity Type

Manufacturer Distributer

Contact Information for Business Card

Vortani

Requirements
Must have
• Names, both office Adresses, email, homepage
Should not have
• Phone Number

```html
<!DOCTYPE html>
<html lang="en">
<head>
<meta charset="utf-8">
<title>VORTANI Business Card</title>
<link rel="stylesheet" href="https://fonts.googleapis.com/css2?family=Arimo:wght@400;700&display=swap">
<style>
  :root {
    --page-bg: #e9e6e1;
    --brand-orange: #e29a1f;
    --panel-dark: #4a4a4b;
    --panel-mid: #545455;
    --panel-deep: #414142;
    --text-light: #ffffff;
    --text-dark: #333333;
    --text-muted: #5a4a30;
    --divider: #2f6b4f;
  }
  * { margin: 0; padding: 0; box-sizing: border-box; }
  html, body { width: 1200px; height: 900px; overflow: hidden; }
  body {
    background: var(--page-bg);
    font-family: "Arimo", Arial, sans-serif;
    display: flex;
    flex-direction: column;
    align-items: center;
    justify-content: center;
    gap: 40px;
  }
  .card {
    position: relative;
    width: 700px;
    height: 400px;
    overflow: hidden;
    border-radius: 4px;
    box-shadow: 0 10px 28px rgba(0,0,0,0.22);
  }
  .card-shape { position: absolute; inset: 0; width: 100%; height: 100%; }
  .brand {
    position: absolute;
    display: flex;
    align-items: center;
    gap: 12px;
    color: var(--text-light);
    font-weight: 400;
    letter-spacing: 1px;
    white-space: nowrap;
  }
  .brand-dot { border-radius: 50%; background: var(--text-light); flex-shrink: 0; }

  /* Front side */
  .card-front .brand { left: 235px; top: 62px; font-size: 46px; }
  .card-front .brand-dot { width: 40px; height: 40px; }
  .service-list {
    position: absolute;
    list-style: none;
    color: var(--text-light);
    font-size: 17px;
    line-height: 23px;
    white-space: nowrap;
  }
  .service-list li { display: flex; align-items: center; gap: 8px; }
  .service-list li::before {
    content: "";
    width: 9px; height: 9px;
    border-radius: 50%;
    background: var(--brand-orange);
    flex-shrink: 0;
  }
  .services-left { left: 22px; top: 262px; }
  .services-right { left: 478px; top: 302px; }
  .website {
    position: absolute;
    left: 233px; width: 234px;
    top: 262px;
    text-align: center;
    color: var(--text-light);
    font-size: 18px;
  }
  .website svg { display: block; margin: 0 auto 22px; }

  /* Back side */
  .owners {
    position: absolute;
    left: 34px; top: 50px;
    color: var(--text-dark);
    font-size: 21px;
    font-weight: 700;
    line-height: 24px;
    white-space: nowrap;
  }
  .owner-role { font-size: 15px; font-weight: 400; color: var(--text-muted); margin-left: 4px; }
  .card-back .brand { right: 36px; top: 26px; font-size: 26px; gap: 8px; }
  .card-back .brand-dot { width: 22px; height: 22px; }
  .contact-block {
    position: absolute;
    width: 233px;
    text-align: center;
    color: var(--text-light);
    font-size: 14px;
    line-height: 18px;
    white-space: nowrap;
  }
  .contact-block.main-office { left: 0; top: 268px; }
  .contact-block.email { left: 233px; top: 240px; }
  .contact-block.branch-office { left: 467px; top: 130px; }
  .contact-icon {
    width: 28px; height: 28px;
    margin: 0 auto 10px;
    border-radius: 50%;
    background: var(--text-light);
    display: flex; align-items: center; justify-content: center;
  }
  .contact-heading { font-weight: 700; text-decoration: underline; }
</style>
</head>
<body>

  <!-- Front -->
  <section class="card card-front" aria-label="Business card front">
    <svg class="card-shape" viewBox="0 0 700 400" preserveAspectRatio="none" aria-hidden="true">
      <defs>
        <filter id="wave-shadow-front" x="-5%" y="-5%" width="110%" height="130%">
          <feDropShadow dx="0" dy="6" stdDeviation="6" flood-color="#000" flood-opacity="0.45"/>
        </filter>
      </defs>
      <rect x="0" y="0" width="234" height="400" fill="var(--panel-dark)"/>
      <rect x="234" y="0" width="233" height="400" fill="var(--panel-deep)"/>
      <rect x="467" y="0" width="233" height="400" fill="var(--panel-mid)"/>
      <line x1="234" y1="0" x2="234" y2="400" stroke="var(--divider)" stroke-width="1.5"/>
      <path filter="url(#wave-shadow-front)" fill="var(--brand-orange)"
        d="M0,0 H700 V210 C640,205 600,195 540,175 C470,150 420,110 340,115 C260,120 210,170 140,175 C80,180 40,165 0,160 Z"/>
    </svg>

    <div class="brand"><span class="brand-dot"></span><span class="brand-name">VORTANI</span></div>

    <ul class="service-list services-left">
      <li>Private Labeling</li>
      <li>High Quality Production</li>
      <li>Direct Distribution</li>
    </ul>

    <div class="website">
      <svg width="32" height="32" viewBox="0 0 32 32" fill="none" stroke="#fff" stroke-width="1.8" aria-hidden="true">
        <circle cx="16" cy="16" r="14"/>
        <ellipse cx="16" cy="16" rx="6" ry="14"/>
        <line x1="2" y1="16" x2="30" y2="16"/>
        <path d="M5 8 H27 M5 24 H27"/>
      </svg>
      vortani-example.com
    </div>

    <ul class="service-list services-right">
      <li>Warehousing</li>
      <li>Trademark Registration</li>
      <li>Legal Support</li>
    </ul>
  </section>

  <!-- Back -->
  <section class="card card-back" aria-label="Business card back">
    <svg class="card-shape" viewBox="0 0 700 400" preserveAspectRatio="none" aria-hidden="true">
      <defs>
        <filter id="wave-shadow-back" x="-5%" y="-5%" width="110%" height="130%">
          <feDropShadow dx="0" dy="6" stdDeviation="6" flood-color="#000" flood-opacity="0.45"/>
        </filter>
      </defs>
      <rect x="0" y="0" width="234" height="400" fill="var(--panel-dark)"/>
      <rect x="234" y="0" width="233" height="400" fill="var(--panel-mid)"/>
      <rect x="467" y="0" width="233" height="400" fill="var(--panel-dark)"/>
      <line x1="234" y1="0" x2="234" y2="400" stroke="var(--panel-deep)" stroke-width="1.5"/>
      <line x1="467" y1="0" x2="467" y2="400" stroke="var(--panel-deep)" stroke-width="1.5"/>
      <path filter="url(#wave-shadow-back)" fill="var(--brand-orange)"
        d="M0,0 H700 V105 C640,95 580,80 520,100 C440,125 400,215 320,225 C240,235 180,190 120,200 C70,208 30,225 0,235 Z"/>
    </svg>

    <div class="owners">
      <div>Lukas Feldhaus<span class="owner-role">Owner</span></div>
      <div>Imran Qureshi<span class="owner-role">Owner</span></div>
    </div>

    <div class="brand"><span class="brand-dot"></span><span class="brand-name">VORTANI</span></div>

    <div class="contact-block main-office">
      <div class="contact-icon">
        <svg width="16" height="16" viewBox="0 0 16 16" aria-hidden="true">
          <path d="M8 2 L14 8 H12 V14 H4 V8 H2 Z" fill="var(--brand-orange)"/>
        </svg>
      </div>
      <div class="contact-heading">Main Office:</div>
      <div>Kornblumenweg 14</div>
      <div>08352 Lindenfeld</div>
      <div>Germany</div>
    </div>

    <div class="contact-block email">
      <div class="contact-icon">
        <svg width="16" height="16" viewBox="0 0 16 16" aria-hidden="true">
          <rect x="2" y="4" width="12" height="8" fill="var(--brand-orange)"/>
          <path d="M2 4 L8 9 L14 4" fill="none" stroke="#fff" stroke-width="1.2"/>
        </svg>
      </div>
      <div>lukas@vortani-example.com</div>
      <div>imran@vortani-example.com</div>
    </div>

    <div class="contact-block branch-office">
      <div class="contact-icon">
        <svg width="16" height="16" viewBox="0 0 16 16" aria-hidden="true">
          <path d="M8 2 L14 8 H12 V14 H4 V8 H2 Z" fill="var(--brand-orange)"/>
        </svg>
      </div>
      <div class="contact-heading">Branch Office:</div>
      <div>Daska Lane</div>
      <div>Rahimabad</div>
      <div>Pakistan</div>
    </div>
  </section>

</body>
</html>
```